vantrelo corporate presentation

We have a wireframe presentation with 18 slides to be implemented in Google slides (powerpoint optional although we would rather prefer Google slides). Please, be creative and don't take the examples in the wireframe as literal. We also provide the following:

- Color palet
- vantrelo Logos
- Slide wireframe
- slide reference for slide number 5.
- Flyer
- Partner logos

You can find all the materials here: https://files.kelvoria.example/share/7qpW3mRtX9vLa2Nc8ZyHbD4FgK1sJe6Uo

```html
<!DOCTYPE html>
<html lang="en">
<head>
<meta charset="utf-8">
<title>vantrelo corporate presentation</title>
<link rel="stylesheet" href="https://fonts.googleapis.com/css2?family=Figtree:wght@400;500&family=Open+Sans:ital,wght@0,300;0,400;0,600;0,700;1,400&display=swap">
<style>
  :root {
    --paper: #ffffff;
    --navy: #0c1528;
    --teal: #14a89c;
    --teal-bright: #00b5a5;
    --white: #ffffff;
  }
  * { box-sizing: border-box; margin: 0; padding: 0; }
  html, body {
    width: 1200px; height: 675px; overflow: hidden;
    background: var(--paper);
  }
  .board { position: relative; width: 1200px; height: 675px; }

  .slide {
    position: absolute; width: 492px; height: 276px; overflow: hidden;
    background: var(--navy);
    font-family: "Open Sans", sans-serif;
  }
  .slide--title { left: 70px; top: 47px; }
  .slide--quote { left: 614px; top: 71px; }
  .slide--about { left: 344px; top: 378px; height: 277px; }

  .brand {
    position: absolute; display: flex; align-items: center; gap: 3px;
    font-family: "Open Sans", sans-serif; font-weight: 700;
    color: var(--white); letter-spacing: -0.02em; line-height: 1;
  }
  .brand__dot { background: var(--teal); display: block; }
  .slide--title .brand { left: 19px; top: 18px; font-size: 17px; }
  .slide--title .brand__dot { width: 8px; height: 8px; }
  .side-panel .brand { left: 18px; top: 20px; font-size: 10px; }
  .side-panel .brand__dot { width: 5px; height: 5px; }

  .title-glow {
    position: absolute; inset: 0;
    background:
      radial-gradient(ellipse 130px 80px at 262px 236px, rgba(0,181,165,0.95), rgba(0,181,165,0) 100%),
      radial-gradient(ellipse 150px 70px at 470px 170px, rgba(150,12,120,0.95), rgba(150,12,120,0) 100%),
      radial-gradient(ellipse 140px 70px at 440px 270px, rgba(80,25,160,0.95), rgba(80,25,160,0) 100%),
      radial-gradient(ellipse 160px 70px at 60px 290px, rgba(110,20,140,0.95), rgba(110,20,140,0) 100%),
      radial-gradient(ellipse 180px 80px at 140px 190px, rgba(20,90,130,0.9), rgba(20,90,130,0) 100%),
      radial-gradient(ellipse 220px 60px at 300px 300px, rgba(25,70,170,0.8), rgba(25,70,170,0) 100%),
      var(--navy);
  }
  .frame-line { position: absolute; background: var(--teal); }
  .slide__title {
    position: absolute; left: 90px; top: 94px; width: 320px;
    font-family: "Figtree", sans-serif; font-weight: 400;
    font-size: 27px; line-height: 31px; color: var(--white);
    text-align: center; letter-spacing: -0.01em;
  }
  .speaker {
    position: absolute; left: 308px; top: 197px;
    color: var(--white); font-size: 9.5px; line-height: 11px;
  }
  .speaker__meta { font-size: 8.5px; }

  .side-panel {
    position: absolute; left: 0; top: 0; width: 88px; height: 100%;
    background: linear-gradient(180deg, var(--navy) 0%, var(--navy) 22%, #0f4a66 40%, #155a8a 58%, #1d3f8c 72%, #5a1d8c 100%);
  }
  .divider-white {
    position: absolute; left: 88px; top: 0; width: 3px; height: 265px;
    background: var(--white);
  }
  .section-label {
    position: absolute; right: 414px; top: 63px;
    font-weight: 300; font-size: 19px; line-height: 16px;
    color: var(--teal); text-align: right;
  }
  .photo { position: absolute; left: 91px; top: 0; right: 0; height: 265px; }
  .photo--tunnel {
    background:
      radial-gradient(ellipse 70px 55px at 175px 95px, #02060f 0%, #02060f 40%, rgba(2,6,15,0) 100%),
      radial-gradient(ellipse 240px 120px at 190px 70px, rgba(40,110,230,0.9), rgba(20,60,160,0.4) 55%, rgba(5,12,30,0) 100%),
      linear-gradient(180deg, #0a1a3c 0%, #071430 60%, #040a18 100%);
  }
  .photo--crowd {
    background:
      radial-gradient(ellipse 260px 90px at 230px 60px, rgba(170,180,190,0.75), rgba(170,180,190,0) 100%),
      linear-gradient(180deg, #8e98a3 0%, #5f6b79 45%, #1f2a3c 80%, #111a2c 100%);
  }
  .bottom-band {
    position: absolute; left: 91px; right: 0; bottom: 0; height: 11px;
    background: linear-gradient(90deg, #4a1c86 0%, #136a8c 30%, #0aa394 50%, #1b4fb0 75%, #4c1f9a 100%);
  }
  .quote {
    position: absolute; left: 107px; top: 153px; width: 132px;
    font-size: 9.4px; line-height: 11.5px; color: var(--teal);
  }
  .quote__source { display: block; font-style: italic; }

  .claim {
    position: absolute; left: 107px; top: 150px;
    font-size: 17px; line-height: 20.5px; color: var(--teal-bright);
  }
  .intro-box {
    position: absolute; left: 268px; right: 0; top: 144px; height: 75px;
    background: var(--teal); padding: 15px 26px 0 21px;
    color: var(--white); font-size: 8.6px; line-height: 9.9px;
  }
</style>
</head>
<body>
<main class="board">

  <section class="slide slide--title">
    <div class="title-glow"></div>
    <div class="brand"><span class="brand__dot"></span>vantrelo</div>
    <div class="frame-line" style="left:26px;top:61px;width:58px;height:1px"></div>
    <div class="frame-line" style="left:84px;top:61px;width:1px;height:130px"></div>
    <div class="frame-line" style="left:84px;top:190px;width:408px;height:1px"></div>
    <h1 class="slide__title">Leading the future<br>with Data and Intelligence</h1>
    <p class="speaker">Marta Velasco<br><span class="speaker__meta">Madrid, 11 Junio</span></p>
  </section>

  <section class="slide slide--quote">
    <div class="side-panel">
      <div class="brand"><span class="brand__dot"></span>vantrelo</div>
    </div>
    <div class="photo photo--tunnel" role="img" aria-label="Photograph of a dark futuristic tunnel lit by blue ring lights"></div>
    <div class="divider-white"></div>
    <div class="bottom-band"></div>
    <div class="frame-line" style="left:25px;top:60px;width:59px;height:1px"></div>
    <div class="frame-line" style="left:84px;top:60px;width:1px;height:202px"></div>
    <div class="frame-line" style="left:84px;top:262px;width:408px;height:1px"></div>
    <h2 class="section-label">the<br>future is<br>now</h2>
    <blockquote class="quote">“Generative AI has the potential to add trillions of dollars in value to the global economy and accelerate productivity growth for individuals, businesses and the economy as a whole.”<span class="quote__source">- Harlow &amp; Pine Partners</span></blockquote>
  </section>

  <section class="slide slide--about">
    <div class="side-panel">
      <div class="brand"><span class="brand__dot"></span>vantrelo</div>
    </div>
    <div class="photo photo--crowd" role="img" aria-label="Overhead photograph of people walking through a busy station concourse"></div>
    <div class="divider-white"></div>
    <div class="bottom-band"></div>
    <div class="frame-line" style="left:24px;top:60px;width:60px;height:1px"></div>
    <div class="frame-line" style="left:84px;top:60px;width:1px;height:201px"></div>
    <div class="frame-line" style="left:84px;top:261px;width:408px;height:1px"></div>
    <h2 class="section-label">about<br>us</h2>
    <p class="claim">Data Analytics<br>and AI for<br>Nonconformists</p>
    <p class="intro-box">We are a leading Professional Services Company specialized in design and implementation of cutting edge technologies in Cloud, Data analytics &amp; AI.</p>
  </section>

</main>
</body>
</html>
```